One page financial canvas needed

I am in the process of developing a financial planning process that uses a one page canvas as a tool for financial education and to explain simple and complex financial strategies to clients. I have the layout and content sorted, just need a hand making it look professional.

It should be a fairly simple project and i have attached a very rough hand drawn canvas showing the desired layout and content. Please feel free to be creative with the design keeping in mind this layout has been chosen to achieve certain outcomes.

Target Market(s)

25-45 Year old Homeowners who are interested in taking better care of the finances

Industry/Entity Type

Financial

Colors

Designer to choose colors to be used in the design.

Requirements
Must have
• very close to the layout in the attached file

```html
<!DOCTYPE html>
<html lang="en">
<head>
<meta charset="utf-8">
<title>Financial Planning Canvas</title>
<link rel="stylesheet" href="https://fonts.googleapis.com/css2?family=Source+Sans+3:wght@700;800&display=swap">
<style>
  :root {
    --blue: #00a9e0;
    --blue-dark: #0096cc;
    --orange: #f26122;
    --orange-ring: #f9c6a8;
    --income-fill: #e8f3ec;
    --expense-fill: #eedcd8;
    --panel-top: #ffffff;
    --panel-bottom: #dcdde0;
    --base-grey: #dddee1;
    --white: #ffffff;
  }
  * { box-sizing: border-box; margin: 0; padding: 0; }
  html, body { width: 1200px; height: 833px; overflow: hidden; background: var(--white); }
  body { position: relative; font-family: "Source Sans 3", "Arial", sans-serif; font-weight: 700; }

  .label {
    position: absolute;
    color: var(--white);
    font-size: 23px;
    letter-spacing: 0.3px;
    text-align: center;
    line-height: 1;
  }

  .side-panel {
    position: absolute;
    top: 82px;
    height: 696px;
    background: linear-gradient(to bottom, var(--panel-top) 5%, var(--panel-bottom) 100%);
  }
  .side-panel--left { left: 25px; width: 230px; border-radius: 6px 0 0 8px; }
  .side-panel--right { left: 917px; width: 241px; border-radius: 0 6px 8px 0; }

  .tab {
    position: absolute;
    height: 40px;
    background: var(--blue);
    display: flex;
    align-items: center;
    justify-content: center;
  }
  .tab .label { position: static; }
  .tab--goals { left: 25px; top: 82px; width: 230px; border-radius: 6px 0 0 0; }
  .tab--fears { left: 917px; top: 82px; width: 241px; border-radius: 0 6px 0 0; }
  .tab--frustrations { left: 917px; top: 296px; width: 241px; border-radius: 0 6px 0 0; }
  .tab--partners { left: 917px; top: 512px; width: 241px; border-radius: 0 6px 0 0; }

  .cashflow-board {
    position: absolute;
    left: 255px;
    top: 27px;
    width: 662px;
    height: 666px;
    border-radius: 10px 10px 0 0;
    overflow: hidden;
    box-shadow: 0 0 6px rgba(0,0,0,0.18);
  }
  .quadrant { position: absolute; }
  .quadrant--income { left: 0; top: 0; width: 342px; height: 666px; background: var(--income-fill); }
  .quadrant--expenses { left: 342px; top: 0; width: 320px; height: 666px; background: var(--expense-fill); }
  .divider { position: absolute; left: 341px; top: 43px; width: 2px; height: 623px; background: var(--orange); }
  .board-header {
    position: absolute; left: 0; top: 0; width: 662px; height: 43px;
    background: var(--orange);
  }
  .board-band {
    position: absolute; left: 0; top: 331px; width: 662px; height: 44px;
    background: var(--orange);
  }

  .board-art { position: absolute; left: 0; top: 0; }

  .base-band { position: absolute; left: 25px; top: 692px; width: 1133px; height: 25px; background: var(--blue); border-radius: 4px 4px 0 0; }
  .base-tray { position: absolute; left: 25px; top: 717px; width: 1133px; height: 61px; background: var(--base-grey); border-radius: 0 0 8px 8px; }
</style>
</head>
<body>
  <div class="side-panel side-panel--left"></div>
  <div class="side-panel side-panel--right"></div>

  <div class="tab tab--goals"><span class="label">GOALS</span></div>
  <div class="tab tab--fears"><span class="label">FEARS</span></div>
  <div class="tab tab--frustrations"><span class="label">FRUSTRATIONS</span></div>
  <div class="tab tab--partners"><span class="label">PARTNERS</span></div>

  <div class="cashflow-board">
    <div class="quadrant quadrant--income"></div>
    <div class="quadrant quadrant--expenses"></div>
    <div class="divider"></div>
    <div class="board-header"></div>
    <div class="board-band"></div>
  </div>

  <div class="base-tray"></div>
  <div class="base-band"></div>

  <svg class="board-art" width="1200" height="833" viewBox="0 0 1200 833" aria-hidden="true">
    <ellipse cx="593" cy="377" rx="101" ry="66" fill="var(--orange)" stroke="var(--orange-ring)" stroke-width="4"/>
    <path d="M48 692 V666 Q48 659 55 659 H190 Q195 659 197 665 L203 692 Z" fill="var(--blue)"/>
    <path d="M505 693 A92 55 0 0 1 689 693 Z" fill="var(--blue)"/>
  </svg>

  <span class="label" style="left:255px; top:40px; width:342px;">INCOME</span>
  <span class="label" style="left:597px; top:40px; width:320px;">EXPENSES</span>
  <span class="label" style="left:360px; top:372px; width:136px;">ASSETS</span>
  <span class="label" style="left:695px; top:372px; width:126px;">DEBT</span>
  <span class="label" style="left:493px; top:343px; width:200px; font-size:29px; line-height:1.15;">CASH<br>FLOW</span>
  <span class="label" style="left:48px; top:671px; width:155px;">TIME</span>
  <span class="label" style="left:505px; top:664px; width:184px;">WEALTH</span>
</body>
</html>
```